Real estate team needs a poster design to promote Free Listing competition

Need a poster design to promote a free listing competition we have about to get underway. It will run from Jan 1,2014 - June 30, 2014 (yes, I'm running late getting this piece organized :-) )! To win a free listing from us, videos need to be submitted that show why they should win the competition and get a free listing from us. It is voted on by the general public on our website. Website is currently being modified to incorporate this so it is not 'live' yet. Our team is KTHomesDirect.com.

I'd like to see designs with blue tones as a focus (our logo and branding is in blue), with some other complementary (and wow) colors incorporated. I'd like to have some depth to the poster, and like what I see with 3D text. Since the competition is about clients submitting videos a movie poster style might be appropriate.

It should be eyecatching and want people to investigate more. A catchy phrase could be 'Lights, Camera, SOLD'. Perhaps this in text in 3D, with lights shining on it, and depth behind it...?? The explanation of the contest could be 'Win the listing services of an exceptional, progressive and dynamic real estate team - a winning video is all we need'.

It should include a pointer for more information to FreeListing.KTHomesDirect.com and the date of Jan 1-June 30, 2014, or email FreeListing@KTHomesDirect.com

We would also use this same design on a A4 size postcard, and print ad.
Updates

Hi folks,

I've just uploaded a zip file of a few iterations of our team logo.  Please note though that the .eps files that I have included have the wrong blue in them.  The correct blue (which is shown in some of the .svg, jpg,.png files) is R 73, G102, B151.

Thank you all very much... looking forward to seeing what you will come up with :-)
Reva

Hello,

thank you for the entries so far.  I am liking what I am seeing.

A few thoughts.  I like the emphasis on the words 'Lights, Camera, SOLD' that I am seeing.  I am liking the incorporation of movie lighting and movie cameras as well. I also like the depth, and 3D components that I've seen in some. 

I've seen designs which have no visual of homes for sale, and some which have stock photos of homes for sale, but am now thinking that we do need some visual representation of the fact that the team sell houses.  When there are no houses in the posters then you actually have to read the text to see that we sell houses if you don't know us, but we want people to get the fact that we sell real estate immediately from first glance... so we should somehow get some visuals of houses in here also.

Some nice homes which have Images that I own, and also videos that I own, are at www.82Tornell.com, www.9Griselda.com, www64Harwright.com ...perhaps something of one of these can be incorporated in to give some visuals?

Thanks so much for your efforts
Reva

Hey folks,
I've just uploaded some more photos. 
With some designs that are featuring photos of houses that we have sold very prominently we perhaps should use photos of my own home instead because I am concerned about the new owners protesting about including photos of their home in the poster.  If the photo is small, or transparent it is not as much of a concern, but where it is prominent it may be more appropriate to use a photo/s where we know the owner won't complain (me :-) ).
I also added a couple of photos of the team in case you wanted to use photos of the team in your design... it is not necessary, but I'd prefer the team versus anonymous people :-)
Thanks again for all submissions... I'm so pleased with what we are getting submitted...!
Thanks
Reva 

Target Market(s)

Homeowners aged 30-55+ who are comfortable with technology. Our main demographic are well educated and have professional occupations.

Industry/Entity Type

Progressive

Requirements
Must have
• It should include a link for more information of FreeListing.KTHomesDirect.com and the date of Jan 1-June 30, 2014. Or to email FreeListing@KTHomesDirect.com
Must have our logo incorporated somewhere on the poster.
Nice to have
• Like to show depth in the poster...perhaps a background, then the 3D words of 'Lights, Camera, SOLD', and perhaps a couple of lights and movie camera in the foreground? We're open but in posters that I have seen while looking for ideas I like the ones with some depth to them.
Like blues, and blue tones with some other colors that 'pop'.
Eyecatching.
Would be great to have the explanation of the contest incorporated somewhere on the poster so that people get the idea immediately of what its all about 'Win the listing services of an exceptional, progressive and dynamic real estate team - a winning video is all we need'

```html
<!DOCTYPE html>
<html lang="en">
<head>
<meta charset="utf-8">
<title>Lights Camera SOLD! – Free Listing Competition</title>
<link rel="stylesheet" href="https://fonts.googleapis.com/css2?family=Anton&family=Arimo:wght@400;700&display=swap">
<style>
  :root {
    --page: #f3f3f1;
    --ink-dark: #0f0f10;
    --panel-dark: #1c1b1d;
    --panel-mid: #3a383b;
    --steel-light: #c9c9cc;
    --steel-mid: #7a7a7e;
    --steel-dark: #2a2a2c;
    --pink: #e8297e;
    --pink-deep: #8c1448;
    --white: #ffffff;
    --brand-blue: #496697;
    --sky: #7fb2e6;
    --foliage: #5d7a3a;
    --stone: #8a8072;
  }
  * { margin: 0; padding: 0; box-sizing: border-box; }
  html, body { width: 800px; height: 1200px; overflow: hidden; background: var(--page); }

  .poster {
    position: absolute; left: 20px; top: 40px; width: 760px; height: 1120px;
    background:
      radial-gradient(ellipse at 60% 70%, var(--panel-mid) 0%, var(--panel-dark) 55%, var(--ink-dark) 100%);
    overflow: hidden;
    font-family: "Arimo", Arial, sans-serif;
    color: var(--white);
  }

  .bevel-band {
    position: absolute; left: 0; width: 760px; height: 48px;
    background: linear-gradient(180deg, var(--steel-dark) 0%, var(--steel-mid) 35%, var(--steel-light) 50%, var(--steel-mid) 65%, var(--steel-dark) 100%);
    border-top: 2px solid #111; border-bottom: 2px solid #111;
  }
  .bevel-band::after {
    content: ""; position: absolute; left: 30px; right: 30px; top: 18px; height: 10px;
    background: linear-gradient(180deg, #1a1a1b, #0c0c0d);
    border-radius: 2px;
  }
  .bevel-band--top { top: 0; }
  .bevel-band--bottom { top: 1072px; }

  .house-photo {
    position: absolute; left: 28px; top: 48px; width: 704px; height: 492px;
    background: linear-gradient(180deg, var(--sky) 0%, #b8cfe6 30%, #cfd2d8 45%, var(--foliage) 72%, var(--stone) 100%);
  }

  .brand {
    position: absolute; left: 440px; top: 80px; width: 270px; height: 62px;
    background: var(--white);
    display: flex; align-items: center; gap: 10px; padding: 0 12px;
  }
  .brand__mark { width: 30px; height: 30px; background: var(--brand-blue); flex: none; }
  .brand__name { font-family: "Arimo", Arial, sans-serif; font-weight: 700; font-size: 21px; color: var(--brand-blue); white-space: nowrap; }

  .headline {
    position: absolute; left: 36px; top: 180px;
    font-family: "Anton", Impact, sans-serif;
    font-size: 104px; line-height: 0.98; color: var(--pink);
    -webkit-text-stroke: 2px var(--white);
    text-shadow: 2px 2px 0 var(--pink-deep), 4px 4px 0 var(--pink-deep), 6px 6px 0 var(--pink-deep), 8px 8px 6px rgba(0,0,0,0.55);
  }
  .headline span { display: block; }

  .title-band {
    position: absolute; left: 0; top: 540px; width: 760px; height: 74px;
    background: linear-gradient(180deg, #050505, #1e1e1f 50%, #050505);
    display: flex; align-items: center; justify-content: center;
  }
  .title-band__text {
    font-weight: 700; font-size: 35px; letter-spacing: 2px;
    text-shadow: 0 2px 3px rgba(0,0,0,0.8);
  }

  .date-badge {
    position: absolute; left: 38px; top: 636px; width: 178px; height: 178px; border-radius: 50%;
    background: radial-gradient(circle at 35% 30%, #d5d5d8 0%, #8a8a8e 45%, #3c3c3f 100%);
    border: 3px solid #1a1a1a;
    box-shadow: 0 0 0 2px #9a9a9e, 0 6px 12px rgba(0,0,0,0.6);
    display: flex; flex-direction: column; align-items: center; justify-content: center;
    font-size: 30px; line-height: 1.12; text-align: center;
    text-shadow: 0 1px 2px rgba(0,0,0,0.7);
  }

  .pitch {
    position: absolute; left: 236px; top: 668px; width: 500px;
    font-weight: 700; font-size: 23.5px; line-height: 1.13; letter-spacing: 0.5px;
    text-transform: uppercase;
  }

  .info-bar {
    position: absolute; left: 89px; top: 836px; width: 580px; height: 34px;
    background: linear-gradient(90deg, rgba(0,0,0,0.85), rgba(20,20,20,0.9) 80%, rgba(40,40,40,0.6));
    display: flex; align-items: center; padding-left: 12px;
    color: var(--pink); font-size: 21px; letter-spacing: 1.5px;
  }

  .contact {
    position: absolute; left: 88px; top: 908px;
    font-size: 22px; letter-spacing: 1.6px; line-height: 1.72;
    text-transform: uppercase; color: #e8e8ea;
  }
</style>
</head>
<body>
  <main class="poster">
    <div class="bevel-band bevel-band--top"></div>

    <div class="house-photo" role="img" aria-label="Photo of a large two-storey family home with gables, a stone retaining wall and green gardens under a blue sky"></div>

    <div class="brand">
      <span class="brand__mark"></span>
      <span class="brand__name">KTHomesDirect.com</span>
    </div>

    <h1 class="headline"><span>Lights</span><span>Camera</span><span>SOLD!</span></h1>

    <div class="title-band"><p class="title-band__text">FREE LISTING COMPETITION</p></div>

    <div class="date-badge">
      <span>JAN 1</span><span>to</span><span>JUNE 30</span><span>2014</span>
    </div>

    <p class="pitch">Win the listing services of an exceptional, progressive and dynamic real estate team - a winning video is all we need</p>

    <p class="info-bar">FOR MORE INFORMATION VISIT OR WRITE</p>

    <div class="contact">
      <p>FreeListing.KTHomesDirect.com</p>
      <p>Email FreeListing@KTHomesDirect.com</p>
    </div>

    <div class="bevel-band bevel-band--bottom"></div>
  </main>
</body>
</html>
```